Social Media Overlay for Ormond Real Estate

We need an social media overlay that can be added to a photo of a house that includes our current logo and a call to action of "Just Listed". This needs to be something that we can use for every new house that we list. Attached is our current logo in both company colors, purple and white. An example of a overlay from Plazeo that we like.

Target Market(s)

Social Media Real Estate Community - Real Estate Agents, Brokers, Buyers & Sellers

Industry/Entity Type

Real Estate

Font styles to use
Sans Serif

Colors
6c459b

Requirements
Must have
• the company colors, purple and white and the company logo
Nice to have
• call to action "Just Listed"
• some layered, texture, or 3-D effect
Should not have
• Should be clean and simple; nothing too busy

```html
<!DOCTYPE html>
<html lang="en">
<head>
<meta charset="utf-8">
<title>Ormond Real Estate – Just Listed Overlay</title>
<link href="https://fonts.googleapis.com/css2?family=Exo+2:wght@500&family=Oswald:wght@500&display=swap" rel="stylesheet">
<style>
  :root {
    --stage: #081f7c;
    --brand-purple: #5f2b85;
    --accent-grey: #9a9a9a;
    --wall-white: #f4f4f4;
    --wall-shade: #e9e9e9;
    --frame-white: rgba(255, 255, 255, 0.75);
    --button-top: #4a4a4a;
    --button-bottom: #0f0f0f;
    --label-light: #f2f2f2;
    --label-mid: #a8a8a8;
  }
  * { margin: 0; padding: 0; box-sizing: border-box; }
  html, body {
    width: 1200px;
    height: 1200px;
    overflow: hidden;
    background: var(--stage);
  }
  .overlay-banner {
    position: absolute;
    left: 120px;
    top: 401px;
    width: 960px;
    height: 354px;
    display: block;
  }
  .brand-name {
    font-family: "Exo 2", "Helvetica Neue", Arial, sans-serif;
    font-weight: 500;
    fill: var(--brand-purple);
  }
  .cta-label {
    font-family: "Oswald", "Arial Narrow", sans-serif;
    font-weight: 500;
    letter-spacing: -1px;
  }
</style>
</head>
<body>
  <svg class="overlay-banner" viewBox="0 0 1200 443" xmlns="http://www.w3.org/2000/svg">
    <defs>
      <linearGradient id="wallTone" x1="0" y1="0" x2="1" y2="1">
        <stop offset="0" stop-color="var(--wall-shade)"/>
        <stop offset="0.5" stop-color="var(--wall-white)"/>
        <stop offset="1" stop-color="var(--wall-shade)"/>
      </linearGradient>
      <linearGradient id="photoTone" x1="0" y1="0" x2="0" y2="1">
        <stop offset="0" stop-color="#8fb7dc"/>
        <stop offset="0.35" stop-color="#d9d2c2"/>
        <stop offset="0.55" stop-color="#5d6a4c"/>
        <stop offset="0.7" stop-color="#6f6d70"/>
        <stop offset="1" stop-color="#4e4d52"/>
      </linearGradient>
      <linearGradient id="buttonTone" x1="0" y1="0" x2="0" y2="1">
        <stop offset="0" stop-color="var(--button-top)"/>
        <stop offset="1" stop-color="var(--button-bottom)"/>
      </linearGradient>
      <linearGradient id="labelTone" x1="0" y1="0" x2="0" y2="1">
        <stop offset="0" stop-color="var(--label-light)"/>
        <stop offset="1" stop-color="var(--label-mid)"/>
      </linearGradient>
      <clipPath id="bannerClip"><rect width="1200" height="443"/></clipPath>
    </defs>

    <g clip-path="url(#bannerClip)">
      <rect class="wall" width="1200" height="443" fill="url(#wallTone)"/>

      <polygon class="corner-block" points="0,0 300,0 95,205 0,110" fill="var(--brand-purple)"/>
      <polygon class="corner-accent" points="0,144 58,194 0,250" fill="var(--accent-grey)"/>
      <polygon class="lower-block" points="82,239 194,349 82,461 -30,349" fill="var(--brand-purple)"/>
      <polygon class="lower-accent" points="164,443 224,381 289,443" fill="var(--accent-grey)"/>

      <polygon class="listing-photo" role="img" aria-label="Photo of the listed house at dusk with a paved driveway"
               points="364,-20 606,221 364,463 122,221" fill="url(#photoTone)"/>
      <polygon class="photo-frame" points="364,8 578,221 364,435 150,221"
               fill="none" stroke="var(--frame-white)" stroke-width="7"/>

      <text class="brand-name" x="868" y="204" font-size="150" text-anchor="middle">Ormond</text>
      <text class="brand-name" x="868" y="282" font-size="74" text-anchor="middle">Real Estate</text>

      <g class="cta-button">
        <rect x="728" y="318" width="287" height="82" rx="34" fill="url(#buttonTone)"/>
        <text class="cta-label" x="871" y="375" font-size="44" text-anchor="middle" fill="url(#labelTone)">JUST LISTED</text>
      </g>
    </g>
  </svg>
</body>
</html>
```